Migration Lawyers

Company: Dunstan & Co Lawyers & Migration Agents

Name: Graham Dunstan BEc, LLB
Address: Level 18, 72 Hollis Street
Sydney, NSW, Australia 2000

Ph: +61 2 9384 5207
M: 0428316540
E: graham@permitpath-example.org.au
W: www.permitpath-example.org.au

Target Market(s)

Migration Clients

Industry/Entity Type

It Company

Font styles to use
Script

Requirements
Must have
• Logo
Should not have
• Please scale the format to the printing size attached

```html
<!DOCTYPE html>
<html lang="en">
<head>
<meta charset="utf-8">
<title>Dunstan &amp; Co — Business Cards</title>
<link rel="stylesheet" href="https://fonts.googleapis.com/css2?family=Tinos:ital,wght@0,400;0,700;1,400&display=swap">
<style>
  :root {
    --page-bg: #d9d9d9;
    --card-white: #ffffff;
    --card-black: #050505;
    --ink: #111111;
    --ink-soft: #3a3a3a;
    --rule: #b5b5b5;
    --reverse-ink: #f2f2f2;
  }
  * { box-sizing: border-box; margin: 0; padding: 0; }
  html, body { width: 1200px; height: 900px; overflow: hidden; }
  body {
    background: var(--page-bg);
    font-family: "Tinos", "Times New Roman", serif;
    color: var(--ink);
    display: flex;
    flex-direction: column;
    align-items: center;
    justify-content: center;
    gap: 60px;
  }
  .card {
    width: 600px;
    height: 367px;
    background: var(--card-white);
    box-shadow: 0 6px 18px rgba(0,0,0,0.18);
    display: flex;
    overflow: hidden;
  }

  /* Back card: contact details */
  .card--contact .brand-panel {
    width: 240px;
    background: var(--card-black);
    display: flex;
    align-items: center;
    justify-content: center;
    gap: 12px;
    padding: 0 18px;
  }
  .brand-panel .brand-circle {
    width: 34px; height: 34px; flex: none;
    border: 2px solid var(--reverse-ink);
    border-radius: 50%;
  }
  .brand-panel .brand-name {
    color: var(--reverse-ink);
    font-weight: 700;
    font-size: 22px;
    line-height: 1.1;
  }
  .contact-panel {
    flex: 1;
    padding: 40px 30px 0 40px;
  }
  .person-name {
    font-weight: 700;
    font-size: 22px;
    letter-spacing: 0.3px;
  }
  .address {
    margin-top: 6px;
    font-style: italic;
    font-size: 12.5px;
    line-height: 1.35;
    color: var(--ink-soft);
  }
  .contact-list {
    list-style: none;
    margin-top: 48px;
    display: flex;
    flex-direction: column;
    gap: 12px;
  }
  .contact-list li {
    display: flex;
    align-items: center;
    gap: 16px;
    font-size: 14px;
    color: var(--ink-soft);
  }
  .contact-list svg { width: 14px; height: 14px; flex: none; }

  /* Front card: brand */
  .card--brand {
    align-items: center;
    justify-content: center;
    gap: 22px;
  }
  .card--brand .brand-circle {
    width: 120px; height: 120px; flex: none;
    border: 2px solid var(--ink);
    border-radius: 50%;
  }
  .card--brand .brand-name {
    font-weight: 700;
    color: var(--ink);
    line-height: 1.05;
  }
  .brand-name .brand-line-main { display: block; font-size: 46px; }
  .brand-name .brand-line-sub { display: block; font-size: 19px; margin-top: 6px; }
</style>
</head>
<body>

  <section class="card card--contact">
    <div class="brand-panel">
      <span class="brand-circle"></span>
      <span class="brand-name">Dunstan &amp; Co</span>
    </div>
    <div class="contact-panel">
      <h1 class="person-name">Graham Dunstan BEc, LLB</h1>
      <p class="address">Level 18, 72 Hollis Street<br>Australia, Sydney, NSW , 2000</p>
      <ul class="contact-list">
        <li>
          <svg viewBox="0 0 16 16" aria-hidden="true"><path d="M3.5 1.5l2.5 3-1.5 1.5c.8 2 2.5 3.7 4.5 4.5L10.5 9l3 2.5-1.5 2.5C7 14 2 9 2 3z" fill="#222"/></svg>
          +61 2 9384 5207
        </li>
        <li>
          <svg viewBox="0 0 16 16" aria-hidden="true"><rect x="2.5" y="2.5" width="11" height="11" fill="none" stroke="#222" stroke-width="1.5"/></svg>
          0428316540
        </li>
        <li>
          <svg viewBox="0 0 16 16" aria-hidden="true"><rect x="1.5" y="3.5" width="13" height="9" fill="#222"/><path d="M1.5 3.5l6.5 5 6.5-5" fill="none" stroke="#fff" stroke-width="1.2"/></svg>
          graham@permitpath-example.org.au
        </li>
        <li>
          <svg viewBox="0 0 16 16" aria-hidden="true"><rect x="1.5" y="2.5" width="13" height="9" fill="none" stroke="#222" stroke-width="1.5"/><path d="M5 14h6M8 11.5V14" stroke="#222" stroke-width="1.5"/></svg>
          www.permitpath-example.org.au
        </li>
      </ul>
    </div>
  </section>

  <section class="card card--brand">
    <span class="brand-circle"></span>
    <p class="brand-name">
      <span class="brand-line-main">Dunstan &amp; Co</span>
      <span class="brand-line-sub">Lawyers &amp; Migration Agents</span>
    </p>
  </section>

</body>
</html>
```